Design a book cover - Quit Telling Us What To Do.....We Decide!!

I need a very cool book cover design including inside flaps and back cover as well as front cover. This is a book for people starting a business or wanting to start a business. My demographic is young. Women who are in the late teens through early 30s. Use their angst and refusal to conform as a guide. Be creative

The title is
Quit Telling Us What To Do.....We Decide

Notes from a Trailblazer:
12 truths gathered along a road toward independence and wealth

Author - Marisol Pendry, MBA, MIB

SIZE is 5 1/2" x 8 1/2"

Be Creative!! And ask questions. PLEASE NO CLIP ART OR CLICHE' type covers!!!!!!! I want your creativity.

```html
<!DOCTYPE html>
<html lang="en">
<head>
<meta charset="UTF-8">
<title>Quit Telling Us What To Do.....We Decide!! — Book Cover</title>
<link rel="stylesheet" href="https://fonts.googleapis.com/css2?family=Bebas+Neue&family=Oswald:wght@500;600&display=swap">
<style>
  :root {
    --page-bg: #e6e6e6;
    --paper: #ffffff;
    --ink: #2d2d2d;
    --magenta: #8e1552;
    --magenta-glow: #e0127a;
    --magenta-text: #8f1a55;
    --on-magenta: #ffffff;
  }
  * { margin: 0; padding: 0; box-sizing: border-box; }
  html, body {
    width: 1200px;
    height: 919px;
    overflow: hidden;
  }
  body {
    background: radial-gradient(ellipse at 45% 40%, #f7f7f7 0%, var(--page-bg) 100%);
    position: relative;
  }
  .cover {
    position: absolute;
    left: 320px;
    top: 30px;
    width: 560px;
    height: 860px;
    overflow: hidden;
    box-shadow: 0 6px 22px rgba(0,0,0,0.18);
  }
  .cover__art {
    position: absolute;
    inset: 0;
  }
  .cover__text {
    position: absolute;
    left: 0;
    width: 100%;
    text-align: center;
  }
  .title-top {
    top: 36px;
    font-family: "Bebas Neue", sans-serif;
    font-size: 94px;
    line-height: 0.98;
    color: var(--ink);
  }
  .title-band {
    top: 290px;
    font-family: "Bebas Neue", sans-serif;
    font-size: 150px;
    line-height: 1;
    color: var(--on-magenta);
    letter-spacing: 1px;
  }
  .subtitle-lead {
    top: 512px;
    font-family: "Oswald", sans-serif;
    font-weight: 600;
    font-size: 31px;
    color: var(--magenta-text);
    text-transform: uppercase;
  }
  .subtitle-body {
    top: 566px;
    display: flex;
    justify-content: center;
    align-items: center;
    gap: 10px;
    font-family: "Oswald", sans-serif;
    font-weight: 600;
    color: var(--ink);
    text-transform: uppercase;
  }
  .subtitle-body__number {
    font-size: 84px;
    line-height: 1;
  }
  .subtitle-body__lines {
    text-align: left;
    font-size: 24px;
    line-height: 1.15;
  }
  .author {
    top: 760px;
    font-family: "Oswald", sans-serif;
    font-weight: 500;
    font-size: 40px;
    color: var(--on-magenta);
    letter-spacing: 1px;
  }
</style>
</head>
<body>
  <div class="cover">
    <svg class="cover__art" width="560" height="860" viewBox="0 0 560 860" aria-hidden="true">
      <defs>
        <radialGradient id="bandGlow" cx="50%" cy="50%" r="60%">
          <stop offset="0%" stop-color="var(--magenta-glow)"/>
          <stop offset="100%" stop-color="var(--magenta)"/>
        </radialGradient>
        <radialGradient id="footGlow" cx="50%" cy="50%" r="70%">
          <stop offset="0%" stop-color="#c41069"/>
          <stop offset="100%" stop-color="var(--magenta)"/>
        </radialGradient>
        <filter id="paperShadow" x="-5%" y="-5%" width="110%" height="115%">
          <feDropShadow dx="0" dy="3" stdDeviation="3" flood-color="#000" flood-opacity="0.35"/>
        </filter>
      </defs>
      <rect class="band band--title" x="0" y="230" width="560" height="270" fill="url(#bandGlow)"/>
      <rect class="band band--author" x="0" y="680" width="560" height="180" fill="url(#footGlow)"/>
      <path class="paper paper--top" fill="var(--paper)" filter="url(#paperShadow)"
        d="M0,0 H560 V254 L532,259 504,251 476,257 448,250 420,258 392,252 364,260 336,253 308,256 280,249 252,258 224,252 196,259 168,251 140,256 112,250 84,258 56,252 28,257 0,251 Z"/>
      <path class="paper paper--middle" fill="var(--paper)" filter="url(#paperShadow)"
        d="M0,478 L28,472 56,480 84,474 112,479 140,471 168,477 196,473 224,481 252,475 280,479 308,472 336,478 364,474 392,480 420,473 448,477 476,471 504,479 532,474 560,478 V700 L532,706 504,698 476,705 448,699 420,707 392,700 364,705 336,698 308,706 280,700 252,704 224,697 196,705 168,699 140,706 112,700 84,704 56,698 28,705 0,700 Z"/>
    </svg>

    <h1 class="cover__text title-top">Quit Telling Us<br>What To Do.....</h1>
    <p class="cover__text title-band">We Decide!!</p>

    <p class="cover__text subtitle-lead">Notes from a Trailblazer:</p>
    <div class="cover__text subtitle-body">
      <span class="subtitle-body__number">12</span>
      <span class="subtitle-body__lines">Truths gathered along a road<br>toward independence and wealth</span>
    </div>

    <p class="cover__text author">MARISOL PENDRY, MBA, MIB</p>
  </div>
</body>
</html>
```